Corvant Systems Business Card

Create an appealing and elegant Business card for corvant systems. Include logo and use related colors from website, be creative. Include Business name, my name, tile, address, contacts, address, and social media contacts if possible. Logo PSD file is attached.

Bleed Area: 3.46" x 2.32"
Trim: 3.3" x 2.16"
Safe Area: 3.14" x 2.02"

Save files as vector-based PDF with outlined text and PNG.
No crop marks
CMYK color setting

Business Card Info:

Corvant Systems

Dennis Halvorsen
Owner

512 Brindlemoor Rd Unit C
Ashgrove Falls, NV 02871
t. 1.888.555.0162
e. dennis.h@corvantsys.example
w. www.corvantsys.example

facebook. www.facebook.com/CorvantSys
twitter. twitter.com/corvantsys
pinterest. www.pinterest.com/corvantsys/

Target Market(s)

Business Owners and Partners

Industry/Entity Type

Business

Requirements
Must have
• Logo and related colors from website

```html
<!DOCTYPE html>
<html lang="en">
<head>
<meta charset="utf-8">
<title>Corvant Systems Business Card</title>
<link href="https://fonts.googleapis.com/css2?family=Bree+Serif&family=Open+Sans:wght@400;600&display=swap" rel="stylesheet">
<style>
  :root {
    --brand-blue: #4d74a6;
    --ink: #1d1d22;
    --body-text: #333338;
    --card-white: #ffffff;
    --backdrop: #d6d7d9;
  }
  * { margin: 0; padding: 0; box-sizing: border-box; }
  html, body { width: 1200px; height: 900px; overflow: hidden; }
  body {
    background: var(--backdrop);
    font-family: "Open Sans", Arial, sans-serif;
    position: relative;
  }
  .card {
    position: absolute;
    top: 280px;
    width: 510px;
    height: 340px;
    background: var(--card-white);
    box-shadow: 0 2px 6px rgba(0,0,0,0.25);
    overflow: hidden;
  }
  .card--front { left: 75px; }
  .card--back { left: 615px; }

  .front-band { position: absolute; inset: 0; }

  .wordmark {
    font-family: "Open Sans", Arial, sans-serif;
    font-weight: 400;
    color: var(--ink);
    line-height: 1.05;
  }
  .front-wordmark {
    position: absolute;
    right: 38px;
    bottom: 40px;
    font-size: 44px;
  }
  .back-wordmark {
    position: absolute;
    left: 38px;
    top: 48px;
    font-size: 29px;
  }

  .social-list {
    position: absolute;
    left: 338px;
    top: 70px;
    list-style: none;
    font-size: 12px;
    color: var(--body-text);
  }
  .social-list li {
    display: flex;
    align-items: center;
    height: 19px;
  }
  .social-dot {
    width: 11px; height: 11px;
    border-radius: 50%;
    background: var(--brand-blue);
    margin-right: 7px;
    flex: none;
  }

  .person {
    position: absolute;
    left: 38px;
    top: 194px;
  }
  .person-name {
    font-family: "Bree Serif", Georgia, serif;
    font-size: 15px;
    color: var(--brand-blue);
    font-weight: 400;
  }
  .person-title {
    font-size: 11px;
    color: var(--body-text);
    margin-top: 4px;
    letter-spacing: 0.3px;
  }

  .divider {
    position: absolute;
    left: 38px;
    right: 38px;
    top: 246px;
    height: 2px;
    background: var(--brand-blue);
  }

  .contact-list {
    position: absolute;
    left: 38px;
    top: 258px;
    list-style: none;
    font-size: 12px;
    color: var(--body-text);
  }
  .contact-list li { height: 19px; display: flex; }
  .contact-label {
    color: var(--brand-blue);
    width: 16px;
    flex: none;
  }

  .office {
    position: absolute;
    left: 322px;
    top: 258px;
    font-size: 12px;
    color: var(--body-text);
    line-height: 19px;
    font-style: normal;
  }
  .office-name {
    color: var(--brand-blue);
    font-weight: 600;
  }
</style>
</head>
<body>
  <section class="card card--front" aria-label="Card front">
    <svg class="front-band" width="510" height="340" viewBox="0 0 510 340" aria-hidden="true">
      <polygon points="0,0 510,0 510,188 210,78 0,258" fill="var(--brand-blue)"/>
    </svg>
    <div class="wordmark front-wordmark">Corvant<br>Systems</div>
  </section>

  <section class="card card--back" aria-label="Card back">
    <div class="wordmark back-wordmark">Corvant<br>Systems</div>

    <ul class="social-list">
      <li><span class="social-dot"></span>/CorvantSys</li>
      <li><span class="social-dot"></span>/corvantsys</li>
      <li><span class="social-dot"></span>/corvantsys/</li>
    </ul>

    <div class="person">
      <h1 class="person-name">Dennis Halvorsen</h1>
      <p class="person-title">OWNER</p>
    </div>

    <div class="divider"></div>

    <ul class="contact-list">
      <li><span class="contact-label">P</span>1.888.555.0162</li>
      <li><span class="contact-label">E</span>dennis.h@corvantsys.example</li>
      <li><span class="contact-label">W</span>www.corvantsys.example</li>
    </ul>

    <address class="office">
      <span class="office-name">Corvant Systems</span><br>
      512 Brindlemoor Rd Unit C<br>
      Ashgrove Falls, NV 02871
    </address>
  </section>
</body>
</html>
```